Website redesign

Looking to redesign our existing website. (quill7meadows.com.au)
New design needs to be bright, fun and have an easy flowing.
The website needs to be design with call to action.

Some examples of other websites:
fernquaylo.com
tovanmilk.com.au

We are happy with the content of our existing website.

Target Market(s)

other businesses

Industry/Entity Type

Business Service

Number of Pages Required

5+ page

Requirements
Must have
• Theme redesign
Cool animation similar to fernquaylo.com

```html
<!DOCTYPE html>
<html lang="en">
<head>
<meta charset="utf-8">
<title>Quill 7 Meadows – Virtual Assistants</title>
<link rel="stylesheet" href="https://fonts.googleapis.com/css2?family=Poppins:wght@300;400;500;600;700&display=swap">
<style>
:root{
  --blue:#17a3df;
  --navy:#0e2233;
  --navy-2:#15293c;
  --navy-3:#0c1b29;
  --ink:#222;
  --muted:#8a8a8a;
  --soft:#f3f3f3;
  --stat:#2b2e31;
  --stat-2:#232629;
  --white:#fff;
}
*{box-sizing:border-box;margin:0;padding:0}
html,body{width:1200px;height:4926px;overflow:hidden}
body{font-family:'Poppins',sans-serif;color:var(--ink);background:var(--white);position:relative}
section,header,footer{position:absolute;left:0;width:1200px;overflow:hidden}
.abs{position:absolute}
.center{left:0;width:1200px;text-align:center}
.btn{position:absolute;height:34px;border-radius:17px;font-size:10px;font-weight:500;text-transform:uppercase;display:flex;align-items:center;justify-content:center;color:var(--white)}
.btn-fill{background:var(--blue)}
.btn-line{border:2px solid var(--white)}
.hex-icon{position:absolute;left:584px;width:32px;height:36px}
.sec-title{position:absolute;left:0;width:1200px;text-align:center;font-size:22px;font-weight:500;color:#2a2a2a}
.sec-text{position:absolute;left:390px;width:420px;text-align:center;font-size:11px;line-height:18px;color:#555}

/* header */
.site-header{top:0;height:71px;background:var(--white)}
.brand{position:absolute;left:162px;top:20px;display:flex;align-items:center;gap:8px;font-weight:600;font-size:14px;color:#1d2b3a}
.brand-dot{width:12px;height:12px;border-radius:50%;background:var(--blue)}
.nav{position:absolute;left:626px;top:28px;display:flex;gap:26px;font-size:10px;font-weight:500;color:#222}
.caret{display:inline-block;border:3.5px solid transparent;border-top-color:#222;margin-left:4px;vertical-align:-1px}

/* hero */
.hero{top:71px;height:460px}
.photo-dark{position:absolute;inset:0;background:linear-gradient(120deg,#4a4d52 0%,#2c2f33 45%,#1c1e21 100%)}
.hero-title{top:92px;font-size:35px;font-weight:700;line-height:52px;color:var(--white)}
.hero-sub{top:210px;font-size:16px;font-weight:500;color:var(--white)}
.arrow{position:absolute;top:211px;width:40px;height:40px;border:2px solid var(--white);border-radius:50%}
.dots{position:absolute;display:flex;gap:8px}
.dots span{width:24px;height:6px;border:1px solid var(--white)}
.dots span.on{background:var(--blue);border-color:var(--blue)}

/* cta band */
.cta-band{top:531px;height:98px;background:var(--navy)}
.cta-band p{position:absolute;left:162px;top:40px;font-size:13px;font-weight:500;color:var(--white)}

/* cards */
.cards{top:629px;height:374px}
.card{position:absolute;top:51px;width:272px}
.card-img{width:272px;height:169px;background:linear-gradient(180deg,#c6d3cb 0%,#9aa89e 60%,#7a5a3a 100%)}
.card h3{margin-top:13px;font-size:12px;font-weight:500;color:#222}
.card p{margin-top:12px;font-size:10.5px;line-height:18px;color:#8a8a8a}

/* work */
.work{top:1003px;height:790px;background:var(--soft)}
.filters{position:absolute;top:213px;left:422px;display:flex;gap:6px}
.filters span{height:26px;padding:0 15px;background:var(--white);border:1px solid #e1e1e1;font-size:10px;color:#555;display:flex;align-items:center}
.filters span.on{background:var(--blue);color:var(--white);border-color:var(--blue);position:relative}
.filters span.on:after{content:"";position:absolute;left:50%;bottom:-6px;margin-left:-5px;border:5px solid transparent;border-top-color:var(--blue);border-bottom:0}
.grid{position:absolute;left:162px;top:272px;width:878px;display:grid;grid-template-columns:repeat(4,219.5px);grid-auto-rows:219px}
.tile.dark{background:linear-gradient(135deg,#3a4048,#15181c)}
.tile.blue{background:linear-gradient(135deg,#b9c8dd,#6a7f9e)}
.tile.light{background:linear-gradient(135deg,#efe8dc,#c9c2b6)}
.tile.paper{background:linear-gradient(135deg,#f1f1ef,#c9a47c)}
.tile.hover{background:#5a5c5f;position:relative}
.tile.hover .frame{position:absolute;left:16px;top:16px;right:16px;bottom:16px;border:1px solid rgba(255,255,255,.6)}
.tile.hover .lbl{position:absolute;top:70px;width:100%;text-align:center;font-size:10px;color:var(--white)}
.tile.hover .ic{position:absolute;top:96px;width:18px;height:18px;border-radius:50%;background:var(--blue)}

/* company */
.company{top:1793px;height:506px}
.tabs{position:absolute;left:162px;top:230px}
.tab{width:209px;height:36px;margin-bottom:7px;background:#f2f2f2;display:flex;align-items:center;gap:12px;padding-left:12px;font-size:12px;color:var(--blue);clip-path:polygon(0 0,93% 0,100% 50%,93% 100%,0 100%)}
.tab.on{background:var(--blue);color:var(--white)}
.tab i{width:14px;height:14px;border-radius:3px;background:currentColor;display:block}
.company-img{position:absolute;left:388px;top:229px;width:273px;height:181px;border-radius:4px;background:linear-gradient(135deg,#d9dde0,#f2f3f4 55%,#a9d0cc)}
.company h3{position:absolute;left:690px;top:224px;font-size:16px;font-weight:500;color:#2a2a2a}
.company .para{position:absolute;left:690px;top:270px;width:350px;font-size:10.5px;line-height:18px;color:#777}
.ticks{position:absolute;left:690px;top:380px;list-style:none;font-size:10px;color:#777}
.ticks li{height:21px;display:flex;align-items:center;gap:7px}
.ticks li:before{content:"";width:9px;height:9px;border-radius:50%;background:var(--blue)}

/* stats */
.stats{top:2299px;height:187px;display:flex}
.stat{flex:1;background:var(--stat);color:var(--white);text-align:center;padding-top:54px}
.stat:nth-child(even){background:var(--stat-2)}
.stat svg{width:26px;height:26px}
.stat b{display:block;font-size:30px;font-weight:600;line-height:36px;margin-top:2px}
.stat small{display:block;font-size:11px;margin-top:2px}

/* feature */
.feature{top:2486px;height:380px}
.feature-img{position:absolute;left:162px;top:75px;width:423px;height:229px;background:linear-gradient(100deg,#d8d4cf,#f0ece8 45%,#6a4a30 80%,#cfc8c0)}
.feature h3{position:absolute;left:613px;top:72px;font-size:16px;font-weight:500;color:#2a2a2a}
.feature .para{position:absolute;left:613px;top:104px;width:420px;font-size:10.5px;line-height:18px;color:#777}
.fitem{position:absolute;left:613px;width:420px}
.fitem svg{position:absolute;left:0;top:2px;width:22px;height:22px}
.fitem h4{margin-left:54px;font-size:11.5px;font-weight:500;color:#222}
.fitem p{margin-left:54px;font-size:10.5px;color:#777;margin-top:2px}

/* cta 2 */
.cta-photo{top:2866px;height:297px}
.cta-photo h2{top:80px;font-size:24px;font-weight:700;color:var(--white)}
.cta-photo p{top:116px;font-size:16px;font-weight:500;color:var(--white)}

/* team */
.team{top:3163px;height:483px}
.team h3{position:absolute;left:208px;top:67px;font-size:16px;font-weight:500;color:#222}
.team .lead{position:absolute;left:208px;top:90px;font-size:11px;color:#777}
.member{position:absolute;top:145px;width:180px;text-align:center}
.hexphoto{width:180px;height:185px;clip-path:polygon(50% 0,100% 25%,100% 75%,50% 100%,0 75%,0 25%);background:linear-gradient(180deg,#4e6260,#6f8ea8 75%,#9fb8d2)}
.member h4{margin-top:15px;font-size:13px;font-weight:500;color:#222}
.member .role{font-size:11px;color:#888;margin-top:4px}
.socials{display:flex;justify-content:center;gap:6px;margin-top:18px}
.socials span{width:22px;height:22px;border-radius:50%;background:#d7d7d7}

/* testimonial */
.testimonial{top:3646px;height:400px}
.avatar{position:absolute;left:569px;top:86px;width:62px;height:62px;border-radius:50%;border:3px solid var(--white);background:linear-gradient(180deg,#b8bcc0,#7f8f9c)}
.quote{position:absolute;left:245px;top:175px;width:710px;text-align:center;font-size:12px;line-height:20px;color:var(--white)}
.quote b{color:var(--blue);font-size:26px;line-height:0;vertical-align:-8px;margin:0 6px}
.testimonial h5{top:259px;font-size:12px;font-weight:500;color:var(--white)}
.testimonial small{position:absolute;top:280px;display:block;font-size:9px;color:var(--white)}

/* subscribe */
.subscribe{top:4046px;height:326px}
.sub-form{position:absolute;left:399px;top:229px;width:402px;height:34px;display:flex}
.sub-form span{flex:1;border:1px solid #ddd;font-size:10px;color:#aaa;display:flex;align-items:center;padding-left:16px}
.sub-form b{width:105px;background:var(--blue);color:var(--white);font-size:10px;font-weight:600;display:flex;align-items:center;justify-content:center}

/* contact */
.contact{top:4372px;height:302px;background:var(--navy-2)}
.contact-panel{position:absolute;left:162px;top:0;width:237px;height:302px;background:var(--navy-3);color:var(--white)}
.contact-panel h3{position:absolute;left:16px;top:20px;font-size:16px;font-weight:600}
.citem{position:absolute;left:16px;display:flex;gap:12px;font-size:10px;line-height:16px}
.citem svg{width:16px;height:16px;margin-top:2px;flex:none}
.big-brand{position:absolute;left:399px;top:118px;width:801px;text-align:center;color:var(--white);font-size:44px;font-weight:600;letter-spacing:1px;display:flex;justify-content:center;align-items:center;gap:18px}
.big-brand i{width:30px;height:30px;border-radius:50%;background:var(--blue)}

/* footer */
.site-footer{top:4674px;height:252px}
.foot-brand{top:48px;font-size:14px;font-weight:600;color:var(--white)}
.foot-social{position:absolute;left:519px;top:105px;display:flex;gap:6px}
.foot-social span{width:28px;height:28px;border-radius:4px;background:var(--blue)}
.copy{top:178px;font-size:10px;color:var(--white)}
</style>
</head>
<body>

<header class="site-header">
  <div class="brand"><i class="brand-dot"></i>QUILL 7 MEADOWS</div>
  <nav class="nav">
    <span>HOME</span><span>ABOUT US</span><span>TIPS AND TRICKS<i class="caret"></i></span><span>OUR SERVICES<i class="caret"></i></span><span>CONTACT US</span>
  </nav>
</header>

<section class="hero">
  <div class="photo-dark" role="img" aria-label="Hands typing on a laptop keyboard, darkened"></div>
  <h1 class="abs center hero-title">VIRTUAL ASSISTANT? MORE LIKE<br>VALUABLE ASSET!</h1>
  <p class="abs center hero-sub">LOREM IPSUM DOLOR SIT AMET, CONSECTETUR ADIPISCING ELIT.</p>
  <span class="btn btn-fill" style="left:544px;top:271px;width:112px">Learn More</span>
  <svg class="arrow" style="left:19px" viewBox="0 0 40 40"><path d="M23 12l-8 8 8 8" fill="none" stroke="#fff" stroke-width="2"/></svg>
  <svg class="arrow" style="left:1135px" viewBox="0 0 40 40"><path d="M17 12l8 8-8 8" fill="none" stroke="#fff" stroke-width="2"/></svg>
  <div class="dots" style="left:556px;top:398px"><span class="on"></span><span></span><span></span></div>
</section>

<section class="cta-band">
  <p>LOREM IPSUM DOLOR SIT AMET, CONSECTETUR ADIPISCING ELIT.</p>
  <span class="btn btn-line" style="left:793px;top:32px;width:110px">Start Now</span>
  <span class="btn btn-fill" style="left:927px;top:32px;width:111px">Learn More</span>
</section>

<section class="cards">
  <article class="card" style="left:162px"><div class="card-img" role="img" aria-label="Vintage camera and pencil pot on a desk"></div><h3>LOREM IPSUM DOLOR SIT AMET</h3><p>Lorem ipsum dolor sit amet, consectetur adipi-scing elit. Duis a orci semper, gravida eros sagit-tis, efficitur orci. Etiam efficitur libero interdum mattis efficitur.</p></article>
  <article class="card" style="left:464px"><div class="card-img" role="img" aria-label="Vintage camera and pencil pot on a desk"></div><h3>LOREM IPSUM DOLOR SIT AMET</h3><p>Lorem ipsum dolor sit amet, consectetur adipi-scing elit. Duis a orci semper, gravida eros sagit-tis, efficitur orci. Etiam efficitur libero interdum mattis efficitur.</p></article>
  <article class="card" style="left:768px"><div class="card-img" role="img" aria-label="Vintage camera and pencil pot on a desk"></div><h3>LOREM IPSUM DOLOR SIT AMET</h3><p>Lorem ipsum dolor sit amet, consectetur adipi-scing elit. Duis a orci semper, gravida eros sagit-tis, efficitur orci. Etiam efficitur libero interdum mattis efficitur.</p></article>
</section>

<section class="work">
  <svg class="hex-icon" style="top:42px" viewBox="0 0 32 36"><polygon points="16,0 32,9 32,27 16,36 0,27 0,9" fill="var(--blue)"/><rect x="10" y="14" width="12" height="9" rx="1" fill="#fff"/></svg>
  <h2 class="sec-title" style="top:90px">OUR AWESOME WORK</h2>
  <p class="sec-text" style="top:143px">Lorem ipsum dolor sit amet, consectetur adipiscing elit. Duis a orci semper, gravida eros sagittis, efficitur orci.</p>
  <div class="filters"><span class="on">All</span><span>Work 01</span><span>Work 01</span><span>Work 01</span><span>Work 01</span></div>
  <div class="grid">
    <div class="tile dark" role="img" aria-label="Laptop screen showing a portfolio page"></div>
    <div class="tile hover" role="img" aria-label="Project preview with hover overlay">
      <div class="frame"></div><div class="lbl">EASY TO LANUNCH</div>
      <i class="ic" style="left:88px"></i><i class="ic" style="left:113px"></i>
    </div>
    <div class="tile blue" role="img" aria-label="Hand using a tablet with a website"></div>
    <div class="tile light" role="img" aria-label="Desktop computer on a white desk"></div>
    <div class="tile dark" role="img" aria-label="Laptop screen showing a portfolio page"></div>
    <div class="tile paper" role="img" aria-label="Kraft paper envelope on white"></div>
    <div class="tile blue" role="img" aria-label="Hand using a tablet with a website"></div>
    <div class="tile dark" role="img" aria-label="Laptop screen showing a portfolio page"></div>
  </div>
</section>

<section class="company">
  <svg class="hex-icon" style="top:43px" viewBox="0 0 32 36"><polygon points="16,0 32,9 32,27 16,36 0,27 0,9" fill="var(--blue)"/><circle cx="16" cy="18" r="5" fill="#fff"/></svg>
  <h2 class="sec-title" style="top:91px">KNOW ABOUT OUR COMPANY</h2>
  <p class="sec-text" style="top:144px">Lorem ipsum dolor sit amet, consectetur adipiscing elit. Duis a orci semper, gravida eros sagittis, efficitur orci.</p>
  <div class="tabs">
    <div class="tab on"><i></i>Who We Are</div>
    <div class="tab"><i></i>Our Company</div>
    <div class="tab"><i></i>What We Do</div>
    <div class="tab"><i></i>Dedicated Support</div>
  </div>
  <div class="company-img" role="img" aria-label="Keyboard, mouse and plant on a white desk"></div>
  <h3>WE ARE AWARD WINNING COMPANY</h3>
  <p class="para">Over the year we have lots of experience in our field. In sit amet massa sapien. Vestibulum diam turpis, gravida in lobor-tis id, ornare a eros. Lorem ipsum dolor sit amet, consectetur adipiscing elit. Aliquam sagittis nulla non elit dignissim suscip-it. Duis lorem nulla, eleifend.</p>
  <ul class="ticks">
    <li>Lorem ipsum dolor sit amet, consectetur adipiscing elit.</li>
    <li>Lorem ipsum dolor sit amet, consectetur adipiscing elit.</li>
    <li>Lorem ipsum dolor sit amet, consectetur adipiscing elit.</li>
  </ul>
</section>

<section class="stats">
  <div class="stat"><svg viewBox="0 0 26 26"><path d="M13 3c-4 0-7 3-7 7v6l-2 3h18l-2-3v-6c0-4-3-7-7-7z" fill="none" stroke="#fff" stroke-width="2"/><circle cx="13" cy="22" r="2" fill="#fff"/></svg><b>5000</b><small>CLIENTS</small></div>
  <div class="stat"><svg viewBox="0 0 26 26"><path d="M13 2L2 8h22z M4 10h18v2H4z M5 13h3v8H5z M11.5 13h3v8h-3z M18 13h3v8h-3z M3 22h20v2H3z" fill="#fff"/></svg><b>2000</b><small>ITEM SOLD</small></div>
  <div class="stat"><svg viewBox="0 0 26 26"><rect x="3" y="8" width="20" height="15" rx="2" fill="#fff"/><rect x="9" y="4" width="8" height="5" rx="1" fill="none" stroke="#fff" stroke-width="2"/></svg><b>500</b><small>PROJECTS</small></div>
  <div class="stat"><svg viewBox="0 0 26 26"><path d="M7 3h12v7a6 6 0 01-12 0z M3 5h4v3a3 3 0 01-4-3z M23 5h-4v3a3 3 0 004-3z M11 16h4v4h-4z M7 21h12v3H7z" fill="#fff"/></svg><b>200</b><small>AWARDS</small></div>
</section>

<section class="feature">
  <div class="feature-img" role="img" aria-label="Coffee cup and pen on a desk"></div>
  <h3>LOREM IPSUM DOLOR SIT AMET, CONSECTETUR</h3>
  <p class="para">Lorem ipsum dolor sit amet, consectetur adipiscing elit. Vivamus ornare magna at massa placerat, in sodales mi finibus. Nam maximus orci id ex hendrerit rutrum.</p>
  <div class="fitem" style="top:187px"><svg viewBox="0 0 22 22"><ellipse cx="11" cy="5" rx="8" ry="3" fill="var(--blue)"/><path d="M3 9c0 2 16 2 16 0v3c0 2-16 2-16 0z M3 15c0 2 16 2 16 0v3c0 2-16 2-16 0z" fill="var(--blue)"/></svg><h4>LOREM IPSUM DOLOR SIT AMET</h4><p>Lorem ipsum dolor sit amet, consectetur adipiscing elit.</p></div>
  <div class="fitem" style="top:256px"><svg viewBox="0 0 22 22"><circle cx="11" cy="11" r="10" fill="var(--blue)"/><path d="M11 5v6l4 3" fill="none" stroke="#fff" stroke-width="2"/></svg><h4>LOREM IPSUM DOLOR SIT AMET</h4><p>Lorem ipsum dolor sit amet, consectetur adipiscing elit.</p></div>
</section>

<section class="cta-photo">
  <div class="photo-dark" role="img" aria-label="Hands on a laptop keyboard, darkened"></div>
  <h2 class="abs center">VIRTUAL ASSISTANT? MORE LIKE VALUABLE ASSET!</h2>
  <p class="abs center">LOREM IPSUM DOLOR SIT AMET, CONSECTETUR ADIPISCING ELIT.</p>
  <span class="btn btn-line" style="left:483px;top:180px;width:111px">Start Now</span>
  <span class="btn btn-fill" style="left:613px;top:180px;width:115px">Get In Touch</span>
</section>

<section class="team">
  <svg class="abs" style="left:160px;top:70px" width="20" height="18" viewBox="0 0 20 18"><path d="M2 2h16v10H8l-4 4v-4H2z" fill="#999"/></svg>
  <h3>MEET WITH OUR TEAM</h3>
  <p class="lead">Lorem ipsum dolor sit amet, consectetur adipiscing elit.</p>
  <div class="member" style="left:162px"><div class="hexphoto" role="img" aria-label="Team member portrait"></div><h4>JOHN DOE</h4><p class="role">Director</p><div class="socials"><span></span><span></span><span></span><span></span><span></span></div></div>
  <div class="member" style="left:395px"><div class="hexphoto" role="img" aria-label="Team member portrait"></div><h4>JOHN DOE</h4><p class="role">Director</p><div class="socials"><span></span><span></span><span></span><span></span><span></span></div></div>
  <div class="member" style="left:621px"><div class="hexphoto" role="img" aria-label="Team member portrait"></div><h4>JOHN DOE</h4><p class="role">Director</p><div class="socials"><span></span><span></span><span></span><span></span><span></span></div></div>
  <div class="member" style="left:848px"><div class="hexphoto" role="img" aria-label="Team member portrait"></div><h4>JOHN DOE</h4><p class="role">Director</p><div class="socials"><span></span><span></span><span></span><span></span><span></span></div></div>
</section>

<section class="testimonial">
  <div class="photo-dark" role="img" aria-label="Hands on a laptop keyboard, darkened"></div>
  <div class="avatar" role="img" aria-label="Client portrait"></div>
  <p class="quote"><b>“</b>Lorem ipsum dolor sit amet, consectetur adipiscing elit. Vivamus ornare magna at massa placerat, in sodales mi finibus. Nam maximus orci id ex hendrerit rutrum. Integer nec tincidunt massa, ut blandit nunc. Nullam eu accumsan magna, at mattis mi. Morbi in euismod lectus.<b>”</b></p>
  <h5 class="abs center">JOHN DOE</h5>
  <small class="center">SR. MANAGER</small>
  <div class="dots" style="left:556px;top:314px"><span class="on"></span><span></span><span></span></div>
</section>

<section class="subscribe">
  <svg class="hex-icon" style="top:41px" viewBox="0 0 32 36"><polygon points="16,0 32,9 32,27 16,36 0,27 0,9" fill="var(--blue)"/><path d="M10 15l6-4 6 4v7H10z" fill="#fff"/></svg>
  <h2 class="sec-title" style="top:88px">SUBSCRIBE WITH US</h2>
  <p class="sec-text" style="top:144px">Lorem ipsum dolor sit amet, consectetur adipiscing elit. Duis a orci semper, gravida eros sagittis, efficitur orci.</p>
  <div class="sub-form"><span>Enter Your Email Address</span><b>SUBSCRIBE</b></div>
</section>

<section class="contact">
  <div class="contact-panel">
    <h3>CONTACT US</h3>
    <div class="citem" style="top:67px"><svg viewBox="0 0 16 16"><path d="M8 1a5 5 0 00-5 5c0 4 5 9 5 9s5-5 5-9a5 5 0 00-5-5z" fill="#fff"/><circle cx="8" cy="6" r="2" fill="var(--navy-3)"/></svg><div>Address<br>Lorem ipsum dolor sit amet,</div></div>
    <div class="citem" style="top:121px"><svg viewBox="0 0 16 16"><path d="M3 1l3 1 1 4-2 1a9 9 0 004 4l1-2 4 1 1 3-2 2C7 15 1 9 1 3z" fill="#fff"/></svg><div>Phone<br>+1 123-456-7890</div></div>
    <div class="citem" style="top:174px"><svg viewBox="0 0 16 16"><rect x="1" y="3" width="14" height="10" fill="none" stroke="#fff" stroke-width="1.6"/><path d="M1 3l7 6 7-6" fill="none" stroke="#fff" stroke-width="1.6"/></svg><div>E-Mail<br>info@example.com</div></div>
    <div class="citem" style="top:229px"><svg viewBox="0 0 16 16"><circle cx="8" cy="8" r="7" fill="none" stroke="#fff" stroke-width="1.6"/><path d="M8 4v4l3 2" fill="none" stroke="#fff" stroke-width="1.6"/></svg><div>Office Timing<br>Mon-Saturday, 9:00-5:00</div></div>
  </div>
  <div class="big-brand"><i></i>QUILL 7 MEADOWS</div>
</section>

<footer class="site-footer">
  <div class="photo-dark" role="img" aria-label="City skyline seen through office windows, darkened"></div>
  <p class="abs center foot-brand">QUILL 7 MEADOWS</p>
  <div class="foot-social"><span></span><span></span><span></span><span></span><span></span></div>
  <p class="abs center copy">© 2020 QUILL 7 MEADOWS | ALL RIGHTS RESERVED.</p>
</footer>

</body>
</html>
```